Offshore Energy Projects Management Consultancy needs a business card design

Logo available. We provide teams to deliver engineering consultancy, project management and delivery teams mainly in the offshore renewables sector. The company is all about bringing the right people to a project to deliver the scope.

The business card will be used for all staff.

The business card should be quite simple, vibrant and uncluttered but convey experience, enthusiasm and integration.

Target Market(s)

Energy Project Developers and Tier 1 construction companies

Contact Information for Business Card

Logo should be on the back of the card. I'm happy for the designer to play with the colour of the logo and background colour.

Front of the card should convey all the must have information in a clear and professional manner but without being overly traditional.

Colors

Designer to choose colors to be used in the design.

Requirements
Must have
• Land Line Tel Number, Mobile Tel Number, Email, business address, web address.

```html
<!DOCTYPE html>
<html lang="en">
<head>
<meta charset="utf-8">
<title>Seaward Delivery Group — Business Card</title>
<link href="https://fonts.googleapis.com/css2?family=Lato:wght@400;700&display=swap" rel="stylesheet">
<style>
  :root {
    --page-bg: #f2f9fd;
    --blue-deep: #1b78c4;
    --blue-bright: #23a6e0;
    --band-blue: #1d76bd;
    --name-blue: #1e78c2;
    --text-grey: #6a6a6a;
    --brand-grey: #676767;
    --white: #ffffff;
  }
  * { margin: 0; padding: 0; box-sizing: border-box; }
  html, body {
    width: 1200px; height: 900px; overflow: hidden;
    background: var(--page-bg);
    font-family: "Lato", Arial, sans-serif;
  }
  .canvas { position: relative; width: 1200px; height: 900px; }
  .card {
    position: absolute; left: 301px; width: 598px; height: 342px;
    box-shadow: 0 12px 28px rgba(40, 60, 80, 0.28);
  }
  .card--logo-side {
    top: 88px;
    background: linear-gradient(30deg, var(--blue-deep) 0%, var(--blue-bright) 100%);
    display: flex; align-items: center; justify-content: center;
  }
  .brand {
    display: flex; align-items: center; gap: 14px;
    font-weight: 700; letter-spacing: 0.02em; text-transform: uppercase;
  }
  .brand__dot { width: 22px; height: 22px; border-radius: 50%; flex: none; }
  .card--logo-side .brand { color: var(--white); font-size: 30px; margin-top: -8px; }
  .card--logo-side .brand__dot { background: var(--white); }

  .card--info-side { top: 470px; background: var(--white); }
  .card--info-side .brand {
    position: absolute; left: 30px; top: 110px; width: 240px;
    color: var(--brand-grey); font-size: 24px; line-height: 1.15;
  }
  .card--info-side .brand__dot { background: var(--name-blue); width: 18px; height: 18px; }

  .contact { position: absolute; left: 320px; top: 74px; }
  .contact__name { color: var(--name-blue); font-size: 24px; font-weight: 700; line-height: 1; }
  .contact__role { color: var(--text-grey); font-size: 14px; margin-top: 6px; }
  .contact__list { list-style: none; margin-top: 22px; }
  .contact__item {
    display: flex; align-items: center; gap: 14px;
    color: var(--text-grey); font-size: 17px; height: 26px;
  }
  .contact__icon { width: 18px; height: 18px; flex: none; fill: var(--name-blue); }

  .address-band {
    position: absolute; left: 0; right: 0; top: 292px; height: 28px;
    background: var(--band-blue); color: var(--white);
    font-size: 16px; text-align: center; line-height: 28px;
  }
</style>
</head>
<body>
<main class="canvas">
  <section class="card card--logo-side" aria-label="Card back">
    <div class="brand"><span class="brand__dot"></span><span>Seaward Delivery Group</span></div>
  </section>

  <section class="card card--info-side" aria-label="Card front">
    <div class="brand"><span class="brand__dot"></span><span>Seaward Delivery Group</span></div>

    <div class="contact">
      <p class="contact__name">Daniel Harper</p>
      <p class="contact__role">CEO | Founder</p>
      <ul class="contact__list">
        <li class="contact__item">
          <svg class="contact__icon" viewBox="0 0 24 24"><path d="M6.6 10.8a15.1 15.1 0 0 0 6.6 6.6l2.2-2.2a1 1 0 0 1 1-.25 11.4 11.4 0 0 0 3.6.57 1 1 0 0 1 1 1V20a1 1 0 0 1-1 1A17 17 0 0 1 3 4a1 1 0 0 1 1-1h3.5a1 1 0 0 1 1 1c0 1.25.2 2.45.57 3.57a1 1 0 0 1-.25 1z"/></svg>
          <span>+ 0 123 456 7899</span>
        </li>
        <li class="contact__item">
          <svg class="contact__icon" viewBox="0 0 24 24"><path d="M8 1h8a2 2 0 0 1 2 2v18a2 2 0 0 1-2 2H8a2 2 0 0 1-2-2V3a2 2 0 0 1 2-2zm0 3v14h8V4zm4 15.2a1 1 0 1 0 0 2 1 1 0 0 0 0-2z"/></svg>
          <span>09 555 444 1234</span>
        </li>
        <li class="contact__item">
          <svg class="contact__icon" viewBox="0 0 24 24"><path d="M2 5h20v2.2l-10 6-10-6zm0 4.5 10 6 10-6V19H2z"/></svg>
          <span>lorem@yourwebsite.com</span>
        </li>
        <li class="contact__item">
          <svg class="contact__icon" viewBox="0 0 24 24"><path d="M12 2a10 10 0 1 0 0 20 10 10 0 0 0 0-20zm-1 17.9A8 8 0 0 1 4.1 11L9 15.9V17a2 2 0 0 0 2 2zm6.9-2.5A2 2 0 0 0 16 16h-1v-3a1 1 0 0 0-1-1H8v-2h2a1 1 0 0 0 1-1V7h2a2 2 0 0 0 2-2v-.4a8 8 0 0 1 2.9 12.8z"/></svg>
          <span>www.yourwebsite.com</span>
        </li>
      </ul>
    </div>

    <div class="address-band">2346 First Address Line, Second Address Line, 56324</div>
  </section>
</main>
</body>
</html>
```